Packaging for Hair Fibers Product

We are a start up company looking for a new packaging design for hair building fibers. These are aimed at predominantly men but also women as well. We already have a logo and i have the packaging design from our competitors. We are wanting to keep the look masculine as 90% of our users will be middle aged men. We would like the colours to be black and white but are open to other colours as well.
It will need to have our logo and the following somewhere on the front.
"Instant Fuller & Thicker Hair" & "Natural Hair Building Fibers" "28g" or "Net Weight 28g"
We only need the front of the packaging designed, please make the other sides of the packaging the same colour but blank.
Target Market(s)
Men 25+
Industry/Entity Type
Hair And Beauty
Requirements
Must have
- Logo which i have included. and the following somewhere on the front.
- "Instant Fuller & Thicker Hair" ; "Natural Hair Building Fibers" "28g" or "Net Weight 28g"
Nice to have
- Make it stand out from the competition or similar to the brantiq example.

```html
<!DOCTYPE html>
<html lang="en">
<head>
<meta charset="utf-8">
<title>Fibramax – Hair Building Fibers Front Panel</title>
<link rel="stylesheet" href="https://fonts.googleapis.com/css2?family=Antonio:wght@300;400;600;700&display=swap">
<style>
  :root {
    --ink: #131313;
    --paper: #ffffff;
  }
  * { margin: 0; padding: 0; box-sizing: border-box; }
  html, body {
    width: 1200px;
    height: 1000px;
    overflow: hidden;
    background: var(--paper);
  }
  .canvas {
    position: relative;
    width: 1200px;
    height: 1000px;
    overflow: hidden;
    background: var(--paper);
    font-family: "Antonio", "Arial Narrow", sans-serif;
  }
  .panel-main {
    position: absolute;
    left: 125px;
    top: 0;
    width: 950px;
    height: 803px;
    background: var(--ink);
  }
  .panel-weight {
    position: absolute;
    left: 125px;
    top: 878px;
    width: 950px;
    height: 122px;
    background: var(--ink);
  }
  .brand-square {
    position: absolute;
    left: 548px;
    top: 138px;
    width: 104px;
    height: 104px;
    border: 2px solid var(--paper);
  }
  .brand-name {
    position: absolute;
    left: 0;
    top: 320px;
    width: 1200px;
    text-align: center;
    color: var(--paper);
    font-weight: 300;
    font-size: 48px;
    letter-spacing: 0.55em;
    text-indent: 0.55em;
    line-height: 1;
  }
  .headline {
    position: absolute;
    left: 360px;
    top: 514px;
    color: var(--paper);
    font-weight: 600;
    text-transform: uppercase;
    line-height: 1;
  }
  .headline-line {
    display: block;
    white-space: nowrap;
    transform-origin: left top;
  }
  .headline-line--top {
    font-size: 113px;
    height: 103px;
    transform: scaleX(0.62);
  }
  .headline-line--bottom {
    font-size: 130px;
    transform: scaleX(0.62);
  }
  .ampersand {
    position: absolute;
    left: 726px;
    top: 492px;
    color: var(--paper);
    font-weight: 400;
    font-size: 256px;
    line-height: 1;
  }
  .tagline {
    position: absolute;
    left: 0;
    top: 817px;
    width: 1200px;
    text-align: center;
    color: var(--ink);
    font-weight: 700;
    font-size: 37px;
    line-height: 1;
    letter-spacing: 0.05em;
    text-indent: 0.05em;
  }
  .net-weight {
    position: absolute;
    left: 0;
    top: 926px;
    width: 1200px;
    text-align: center;
    color: var(--paper);
    font-weight: 700;
    font-size: 50px;
    line-height: 1;
    letter-spacing: 3px;
    text-indent: 3px;
  }
</style>
</head>
<body>
  <main class="canvas">
    <section class="panel-main"></section>
    <div class="brand-square" aria-hidden="true"></div>
    <p class="brand-name">FIBRAMAX</p>

    <h1 class="headline">
      <span class="headline-line headline-line--top">Instant Fuller</span>
      <span class="headline-line headline-line--bottom">Thicker Hair</span>
    </h1>
    <span class="ampersand">&amp;</span>

    <p class="tagline">NATURAL HAIR BUILDING FIBERS</p>

    <section class="panel-weight"></section>
    <p class="net-weight">28G</p>
  </main>
</body>
</html>
```